6x11 Postcard for Moving Company

Must have company logo and the company slogan underneath: "The Moving Company You Can Trust And Rely On!". Must have company phone number: 858-555-0142. Must have company email, website and address:
info@haul-pivot.com
www.haul-pivot.com
4127 Penwick Lane, Suite B1,
San Diego, CA 92177
Must have company licenses listed in the following format:
CAL-T# 574318 | CA# 208751 | MC# 362940 | USDOT# 7140829

Must include the following services:
Packing - Moving - Unpacking
Loading - Unloading
Storage In Transit
Long Term Storage
Local - Long Distance
Residential - Commercial
Licensed - Insured
Free Onsite and Video Estimates

And please include the following text above or below the phone number: "Call For FREE Friendly Estimates and Advice!"

Target Market(s)

New Homes that go on sale and Home that were sold and in pending status.

Industry/Entity Type

Moving Company

Colors

Designer to choose colors to be used in the design.

Requirements
Must have
• A photo of a family on the front of the postcard. Must be looking like a real photo of the actual owner of the company with wife and 2 kids (not just a basic stock family photo). Must have Qorvix Assurance Logo and the text "Qorvix Assured". Must say/include 5 star rating on Tarnly, Qorvix, Nestplanner, Chatterwall, Pinbrook. Must include FQC A+ Accreditation Logo. Must include the Certified HaulSure Logo (see attached) and the Golden Haul Expert badege. Must have a Book Online Option. Must leave space for FMDA permit for postage. Must include the following deals: $250 Off Long Distance Moves, $50 Off Local Moves, Free Boxes (*call for details), 1 Month Storage Free. (in smaller text must say: *Offers can not be combined with other offers)

```html
<!DOCTYPE html>
<html lang="en">
<head>
<meta charset="utf-8">
<title>Haul Pivot Postcard</title>
<link rel="stylesheet" href="https://fonts.googleapis.com/css2?family=Oswald:wght@500;700&family=Barlow+Condensed:ital,wght@0,500;0,700;1,700&family=Mulish:wght@600;800&display=swap">
<style>
:root{
  --navy:#2b3a66;
  --navy-deep:#1f2c55;
  --red:#e3212b;
  --red-dark:#c8161f;
  --gold:#f4b223;
  --white:#ffffff;
  --ink:#1d1d1f;
  --qorvix:#4a72c4;
  --pinbrook:#e8742a;
  --stage-top:#1c1c1e;
  --stage-bottom:#555557;
}
*{margin:0;padding:0;box-sizing:border-box}
html,body{width:1073px;height:1200px;overflow:hidden}
body{background:linear-gradient(var(--stage-top) 0 926px,var(--stage-bottom) 926px);position:relative;font-family:'Mulish',sans-serif}
.card{position:absolute;left:82px;width:908px;height:496px;background:var(--white);overflow:hidden}
.front{top:82px}
.back{top:622px}
.abs{position:absolute}
.shape-layer{position:absolute;inset:0}
.brand{font-family:'Oswald',sans-serif;font-weight:700;color:var(--white);letter-spacing:1px;line-height:1;white-space:nowrap}
.front .brand{left:44px;top:44px;font-size:72px}
.slogan{left:46px;top:120px;font-family:'Oswald',sans-serif;font-weight:700;color:var(--white);font-size:32px;line-height:40px;white-space:nowrap}
.cta{left:70px;top:272px;transform:rotate(-10deg);transform-origin:left top}
.cta-free{position:absolute;left:20px;top:0;width:230px;height:62px;background:var(--red);clip-path:polygon(4% 0,100% 0,96% 100%,0 100%);font-family:'Oswald',sans-serif;font-weight:500;color:var(--white);font-size:34px;line-height:62px;padding-left:22px;white-space:nowrap}
.cta-book{position:absolute;left:262px;top:8px;font-family:'Oswald',sans-serif;font-weight:500;color:var(--white);font-size:22px;line-height:24px}
.cta-phone{position:absolute;left:70px;top:58px;width:240px;height:62px;background:var(--red-dark);clip-path:polygon(4% 0,100% 0,96% 100%,0 100%);font-family:'Oswald',sans-serif;font-weight:700;color:var(--white);font-size:36px;line-height:62px;padding-left:14px;white-space:nowrap}
.cta-tag{position:absolute;left:-30px;top:70px;width:100px;height:40px;background:var(--red);clip-path:polygon(0 0,100% 0,100% 100%,8% 100%);font-family:'Barlow Condensed',sans-serif;font-weight:700;color:var(--white);font-size:10px;line-height:11px;text-align:center;padding-top:9px}
.services{left:46px;top:394px;font-weight:800;color:var(--navy);font-size:19.5px;line-height:23.5px}
.divider{width:3px;background:var(--red)}
.list{font-weight:800;font-size:14.5px;line-height:18.5px}
.list-red{left:335px;top:372px;color:var(--red)}
.list-navy{left:594px;top:408px;color:var(--navy)}
.offers{left:46px}
.back .brand{left:46px;top:34px;font-size:66px}
.deal{font-family:'Oswald',sans-serif;font-weight:700;color:var(--red);font-size:48px;line-height:1}
.deal-label{font-family:'Barlow Condensed',sans-serif;font-style:italic;font-weight:700;color:var(--white);font-size:19px}
.rule{height:3px;background:linear-gradient(90deg,var(--white),rgba(255,255,255,0))}
.fine{font-family:'Barlow Condensed',sans-serif;font-weight:500;color:var(--red);font-size:15.5px;line-height:18px}
.contact{font-weight:600;color:var(--white);font-size:15.5px;line-height:19px}
.licenses{font-weight:600;color:var(--red);font-size:15.5px;line-height:19px}
.rating-title{left:548px;top:42px;width:142px;text-align:center;font-family:'Oswald',sans-serif;font-weight:700;color:var(--navy);font-size:18px;line-height:22px;white-space:nowrap}
.site{font-weight:800;font-size:30px;line-height:1}
.site-small{font-weight:800;font-size:14px;line-height:1;color:var(--ink);white-space:nowrap}
.site-mark{width:12px;height:12px;background:var(--navy)}
.stamp{left:782px;top:45px;width:82px;height:82px;background:var(--navy)}
.addr-line{left:534px;width:330px;height:1px;background:var(--ink)}
</style>
</head>
<body>

<section class="card front" aria-label="Postcard front">
  <svg class="shape-layer" viewBox="0 0 908 496" aria-hidden="true">
    <defs>
      <linearGradient id="navyFade" x1="0" y1="0" x2="1" y2="1">
        <stop offset="0" stop-color="#2f3f6d"/>
        <stop offset="1" stop-color="#1f2c55"/>
      </linearGradient>
      <linearGradient id="photoTone" x1="0" y1="0" x2="1" y2="1">
        <stop offset="0" stop-color="#eceff3"/>
        <stop offset="0.5" stop-color="#d9c2a0"/>
        <stop offset="1" stop-color="#c9a97f"/>
      </linearGradient>
    </defs>
    <path d="M0,0 H700 C580,50 560,190 480,280 C420,340 330,362 200,372 C110,380 40,388 0,402 Z" fill="url(#navyFade)"/>
    <path d="M700,0 H908 V258 C860,330 780,360 700,330 C620,300 530,330 440,352 C520,300 570,170 700,0 Z" fill="url(#photoTone)" role="img" aria-label="Photo of a smiling couple sitting among moving boxes"/>
    <path d="M440,352 C530,330 620,300 700,330 C780,360 860,330 908,258" fill="none" stroke="var(--red)" stroke-width="4"/>
  </svg>

  <div class="abs brand">HAULPIVOT</div>
  <div class="abs slogan">THE MOVING COMPANY YOU<br>CAN TRUST AND RELY ON!</div>

  <div class="abs cta">
    <div class="cta-tag">FRIENDLY ESTIMATES<br>AND ADVICE!</div>
    <div class="cta-free">Call for FREE</div>
    <div class="cta-book">BOOK<br>ONLINE</div>
    <div class="cta-phone">858-555-0142</div>
  </div>

  <div class="abs services">● PACKING ● MOVING<br>● UNPACKING<br>● LOADING ● UNLOADING</div>
  <div class="abs divider" style="left:312px;top:368px;height:95px"></div>
  <div class="abs list list-red">STORAGE IN TRANSIT<br>LONG TERM STORAGE<br>LOCAL - LONG DISTANCE<br>RESIDENTIAL - COMMERCIAL<br>LICENSED - INSURED</div>
  <div class="abs divider" style="left:571px;top:388px;height:75px"></div>
  <div class="abs list list-navy">FREE ONSITE AND VIDEO ESTIMATES<br>DAILY INTRA-STATE ROUTES<br>WEEKLY INTER-STATE ROUTES</div>
</section>

<section class="card back" aria-label="Postcard back">
  <svg class="shape-layer" viewBox="0 0 908 496" aria-hidden="true">
    <defs>
      <linearGradient id="backTone" x1="0" y1="0" x2="1" y2="1">
        <stop offset="0" stop-color="#33436f"/>
        <stop offset="1" stop-color="#27365f"/>
      </linearGradient>
      <linearGradient id="whiteFade" x1="0" y1="0" x2="0" y2="1">
        <stop offset="0" stop-color="#eef0f3"/>
        <stop offset="0.5" stop-color="#ffffff"/>
      </linearGradient>
    </defs>
    <rect x="0" y="0" width="454" height="496" fill="url(#backTone)" role="img" aria-label="Faint photo of movers loading a truck"/>
    <rect x="454" y="0" width="454" height="496" fill="url(#whiteFade)" role="img" aria-label="Faded photo of a moving truck"/>
    <path d="M541,53 H488 Q478,53 478,63 V80 Q478,90 488,92 M695,53 H750 Q760,53 760,63 V80 Q760,90 750,92" fill="none" stroke="var(--gold)" stroke-width="3"/>
    <g fill="var(--gold)">
      <polygon id="star" points="518,66 523,79 537,80 526,89 530,103 518,95 506,103 510,89 499,80 513,79"/>
      <use href="#star" x="50"/><use href="#star" x="100"/><use href="#star" x="150"/><use href="#star" x="200"/>
    </g>
    <rect x="484" y="236" width="126" height="48" rx="4" fill="var(--navy)"/>
    <circle cx="654" cy="261" r="28" fill="none" stroke="var(--navy)" stroke-width="3"/>
    <rect x="706" y="237" width="46" height="48" fill="var(--gold)"/>
  </svg>

  <div class="abs brand">HAULPIVOT</div>
  <div class="abs offers deal" style="top:120px">$250 OFF</div>
  <div class="abs offers deal-label" style="top:175px">LONG DISTANCE MOVES</div>
  <div class="abs offers rule" style="top:203px;width:210px"></div>
  <div class="abs offers deal" style="top:216px">$50 OFF</div>
  <div class="abs offers deal-label" style="top:272px">LOCAL MOVES</div>
  <div class="abs offers rule" style="top:300px;width:210px"></div>
  <div class="abs offers fine" style="top:310px">Free Boxes (*call for details),<br>1 Month Storage Free.<br>*Offers can not be combined with other offers.</div>
  <div class="abs offers rule" style="top:368px;width:350px"></div>
  <div class="abs offers contact" style="top:376px">info@haul-pivot.com | www.haul-pivot.com<br>4127 Penwick Lane, Suite B1, San Diego, CA 92177</div>
  <div class="abs offers rule" style="top:420px;width:350px"></div>
  <div class="abs offers licenses" style="top:428px">CAL-T# 574318 | CA# 208751 | MC# 362940<br>USDOT# 7140829</div>

  <div class="abs rating-title">5 STAR RATING ON</div>
  <div class="abs site" style="left:486px;top:142px;color:var(--ink)">Tarnly</div>
  <div class="abs site" style="left:634px;top:140px;color:var(--qorvix)">Qorvix</div>
  <div class="abs site-small" style="left:484px;top:196px">Nestplanner</div>
  <div class="abs site-mark" style="left:588px;top:197px"></div>
  <div class="abs site-small" style="left:604px;top:196px">Chatterwall</div>
  <div class="abs site-small" style="left:700px;top:196px;color:var(--pinbrook)">Pinbrook</div>
  <div class="abs stamp" aria-label="Postage area"></div>
  <div class="abs addr-line" style="top:366px"></div>
  <div class="abs addr-line" style="top:410px"></div>
  <div class="abs addr-line" style="top:454px"></div>
</section>

</body>
</html>
```